Surface Protection company needs cards

We are a New Zealand company that will apply nanotechnology coatings on surfaces to prevent growth and spread of bacteria, viruses, mold etc with a sprayer. We deal with large corporates, airlines, hospitals and schools so we are after a new modern, simple and clean look that will have great visual impact.
We a company that is focused on prevention and protection.

Company name, Vela Shield

Subtext, Antimicrobial Surface Protection

Logo, VS

Target Market(s)

Hospitals, Transport agencies, Airlines, Corporate entities

Contact Information for Business Card

Company name, VelaShield
Logo, VS

Garth Ormsby
velashieldnz@postkite.example
+64219302648
www.velashield.example.nz

Requirements
Must have
• Simple clean look.
Nice to have
• We apply nano coatings so try and incorporate this into a theme somehow

```html
<!DOCTYPE html>
<html lang="en">
<head>
<meta charset="utf-8">
<title>Vela Shield – Business Cards</title>
<link href="https://fonts.googleapis.com/css2?family=Lato:wght@400&family=Michroma&display=swap" rel="stylesheet">
<style>
  :root {
    --bg: #e3e3e3;
    --card: #ffffff;
    --ink: #1d1d1f;
    --blue-dark: #0b6aa2;
    --blue-mid: #1794c8;
    --blue-light: #13b2e3;
    --green-dark: #5a8530;
    --green-mid: #9db22e;
    --lime: #c8d224;
    --icon: #1593d3;
  }
  * { margin: 0; padding: 0; box-sizing: border-box; }
  html, body { width: 1200px; height: 1195px; overflow: hidden; background: var(--bg); }
  .canvas { position: relative; width: 1200px; height: 1195px; }
  .card {
    position: absolute; left: 342px; width: 523px; height: 314px;
    background: var(--card); overflow: hidden;
    box-shadow: 0 2px 6px rgba(0,0,0,.15);
  }
  .card--front { top: 219px; }
  .card--back { top: 630px; }
  .card .waves { position: absolute; inset: 0; width: 100%; height: 100%; }

  .brand { position: absolute; display: flex; flex-direction: column; }
  .brand__row { display: flex; align-items: center; }
  .brand__dot { border-radius: 50%; background: var(--green-mid); flex: none; }
  .brand__name { font-family: "Michroma", sans-serif; font-weight: 400; color: var(--ink); white-space: nowrap; }
  .brand__tagline { font-family: "Lato", sans-serif; color: var(--ink); white-space: nowrap; }

  .card--front .brand { left: 24px; top: 44px; }
  .card--front .brand__dot { width: 16px; height: 16px; margin-right: 12px; }
  .card--front .brand__name { font-size: 19px; letter-spacing: 2px; }
  .card--front .brand__tagline { font-size: 11px; letter-spacing: 2px; margin: 6px 0 0 28px; }

  .contacts { position: absolute; left: 38px; top: 144px; list-style: none; }
  .contacts li { display: flex; align-items: center; height: 23.3px;
    font-family: "Lato", sans-serif; font-size: 13.5px; color: var(--ink); }
  .contacts svg { width: 16px; height: 16px; margin-right: 9px; fill: var(--icon); flex: none; }

  .divider { position: absolute; left: 258px; top: 152px; width: 1.5px; height: 76px; background: var(--ink); }
  .person { position: absolute; left: 269px; top: 167px; }
  .person__name { font-family: "Michroma", sans-serif; font-size: 16px; color: var(--ink); letter-spacing: .5px; white-space: nowrap; }
  .person__role { font-family: "Lato", sans-serif; font-size: 15px; color: var(--ink); margin-top: 1px; }

  .card--back .brand { left: 98px; top: 132px; }
  .card--back .brand__dot { width: 22px; height: 22px; margin-right: 16px; }
  .card--back .brand__name { font-size: 26px; letter-spacing: 3px; }
  .card--back .brand__tagline { font-size: 14px; letter-spacing: 3.4px; margin: 6px 0 0 40px; }
</style>
</head>
<body>
<main class="canvas">

  <section class="card card--front" aria-label="Business card front">
    <svg class="waves" viewBox="0 0 523 314" preserveAspectRatio="none" aria-hidden="true">
      <defs>
        <linearGradient id="frontBlue" x1="0" x2="1">
          <stop offset="0" stop-color="var(--blue-dark)"/>
          <stop offset=".55" stop-color="var(--blue-mid)"/>
          <stop offset="1" stop-color="var(--blue-light)"/>
        </linearGradient>
        <linearGradient id="frontGreen" x1="0" x2="1">
          <stop offset="0" stop-color="var(--green-dark)"/>
          <stop offset=".5" stop-color="var(--green-mid)"/>
          <stop offset="1" stop-color="var(--lime)"/>
        </linearGradient>
      </defs>
      <path d="M0,258 C110,264 220,296 300,295 C400,294 460,265 523,232 L523,314 L0,314 Z" fill="url(#frontBlue)"/>
      <path d="M20,260 L250,258 C370,252 460,205 523,161 L523,216 C470,244 420,268 380,280 C340,292 290,297 250,293 C200,288 160,281 120,275 C80,268 50,262 20,260 Z" fill="url(#frontGreen)"/>
    </svg>

    <div class="brand">
      <div class="brand__row"><span class="brand__dot"></span><span class="brand__name">VELA SHIELD</span></div>
      <span class="brand__tagline">Antimicrobial • Surface • Protection</span>
    </div>

    <ul class="contacts">
      <li><svg viewBox="0 0 16 16"><path d="M8 0a6 6 0 0 0-6 6c0 4.5 6 10 6 10s6-5.5 6-10a6 6 0 0 0-6-6zm0 8.5A2.5 2.5 0 1 1 8 3.5a2.5 2.5 0 0 1 0 5z"/></svg>New Zealand</li>
      <li><svg viewBox="0 0 16 16"><path d="M3.6 1l2.4 3.2-1.5 1.6c.8 2 2.6 3.9 4.7 4.8l1.6-1.5L14 11.5 12.2 14C6.6 13.6 2.2 9.2 2 3.6z"/></svg>+64219302648</li>
      <li><svg viewBox="0 0 16 16"><path d="M0 3h16v10H0zM1.5 4.2v.3L8 9l6.5-4.5v-.3zM1.5 11.8h13L10 7.8 8 9.2 6 7.8z"/></svg>velashieldnz@postkite.example</li>
      <li><svg viewBox="0 0 16 16"><path d="M4 1l9 8H8.6l2.4 5-1.8.8-2.3-5L4 12.5z"/></svg>www.velashield.example.nz</li>
    </ul>

    <span class="divider"></span>
    <div class="person">
      <p class="person__name">GARTH ORMSBY</p>
      <p class="person__role">Solution Manager</p>
    </div>
  </section>

  <section class="card card--back" aria-label="Business card back">
    <svg class="waves" viewBox="0 0 523 314" preserveAspectRatio="none" aria-hidden="true">
      <defs>
        <linearGradient id="backBlue" x1="0" x2="1">
          <stop offset="0" stop-color="var(--blue-dark)"/>
          <stop offset=".6" stop-color="var(--blue-mid)"/>
          <stop offset="1" stop-color="var(--blue-light)"/>
        </linearGradient>
        <linearGradient id="backGreen" x1="0" x2="1">
          <stop offset="0" stop-color="var(--green-dark)"/>
          <stop offset="1" stop-color="var(--green-mid)"/>
        </linearGradient>
        <linearGradient id="backLime" x1="0" x2="1">
          <stop offset="0" stop-color="var(--green-dark)"/>
          <stop offset=".6" stop-color="var(--green-mid)"/>
          <stop offset="1" stop-color="var(--lime)"/>
        </linearGradient>
      </defs>
      <path d="M0,26 C60,42 120,54 170,52 C230,50 290,40 350,40 C420,40 470,55 523,79 L523,58 C470,40 420,33 350,33 C290,33 230,43 170,46 C120,48 60,38 0,28 Z" fill="url(#backBlue)"/>
      <path d="M0,0 H523 V60 C470,42 420,34 350,35 C290,35 230,45 170,48 C120,50 60,40 0,28 Z" fill="url(#backLime)"/>
      <path d="M0,222 C100,270 250,283 350,274 C430,266 480,270 523,285 L523,314 L0,314 Z" fill="url(#backGreen)"/>
      <path d="M0,244 C100,285 240,292 350,280 C430,271 480,275 523,290 L523,314 L0,314 Z" fill="url(#backBlue)"/>
    </svg>

    <div class="brand">
      <div class="brand__row"><span class="brand__dot"></span><span class="brand__name">VELA SHIELD</span></div>
      <span class="brand__tagline">Antimicrobial  Surface  Protection</span>
    </div>
  </section>

</main>
</body>
</html>
```